Brindle Harbor Stationery Design Project

We need complete stationary design for a start up company called "Brindle Harbor". We develop B2B and B2C SAAS based solutions and e-commerce portals for companies. The design should communicate simplicity and elegance. The domain name of the site will be brindleharbor.com. The logo of the company is https://files.quellbox.net/u/4817205/7734_2208615_91437_image.jpg
Updates

Target Market(s)

B2B and B2C

Industry/Entity Type

E-Commerce

Requirements
Must have
• The design should reflect the followings:
- Company logo
- Company activities
- Be modern
Nice to have
• Preferably, the colors of the logo are to be used, but we are open for suggestions.

A design with transparent background might be nice.

```html
<!DOCTYPE html>
<html lang="en">
<head>
<meta charset="utf-8">
<title>Brindle Harbor — Business Cards</title>
<link rel="stylesheet" href="https://fonts.googleapis.com/css2?family=Open+Sans:wght@400;600;700&display=swap">
<style>
  :root {
    --backdrop: #4a4a4a;
    --card: #ffffff;
    --brand-blue: #1a5fa8;
    --band-blue-light: #2c8fd6;
    --band-blue-dark: #1769b4;
    --brand-red: #e01f26;
    --ink: #1e1e1e;
  }
  * { margin: 0; padding: 0; box-sizing: border-box; }
  html, body {
    width: 1200px; height: 900px; overflow: hidden;
    background: var(--backdrop);
    font-family: "Open Sans", Arial, sans-serif;
  }
  .stage { position: relative; width: 1200px; height: 900px; }
  .card {
    position: absolute; top: 300px;
    width: 525px; height: 300px;
    background: var(--card);
    overflow: hidden;
  }
  .card--front { left: 58px; }
  .card--back { left: 617px; }

  .wordmark {
    position: absolute; left: 0; right: 0;
    text-align: center;
    color: var(--brand-blue);
    font-weight: 600;
    letter-spacing: -0.5px;
  }
  .card--front .wordmark { top: 108px; font-size: 38px; }
  .card--back .wordmark { top: 55px; font-size: 19px; }

  .contact { position: absolute; left: 0; right: 0; text-align: center; color: var(--ink); }
  .contact__name { top: 122px; font-size: 17px; font-weight: 700; color: var(--brand-blue); }
  .contact__title { top: 144px; font-size: 10.5px; }
  .contact__address { top: 168px; font-size: 14px; }
  .contact__lines { top: 194px; font-size: 11px; }
  .contact__lines b { color: var(--brand-blue); font-weight: 700; }
  .contact__lines span { margin: 0 4px; }

  .footer-band { position: absolute; left: 0; top: 230px; width: 525px; height: 60px; }
  .site-url {
    position: absolute; left: 0; right: 0; top: 253px;
    text-align: center;
    color: #fff; font-size: 13.5px; letter-spacing: 1.6px;
  }
</style>
</head>
<body>
<main class="stage">

  <section class="card card--front">
    <div class="wordmark">Brindle Harbor</div>
    <svg class="footer-band" viewBox="0 0 525 60" aria-hidden="true">
      <defs>
        <linearGradient id="bandBlue" x1="0" y1="0" x2="0" y2="1">
          <stop offset="0" stop-color="var(--band-blue-light)"/>
          <stop offset="1" stop-color="var(--band-blue-dark)"/>
        </linearGradient>
      </defs>
      <rect x="72" y="3" width="380" height="55" fill="url(#bandBlue)"/>
      <rect x="0" y="56" width="525" height="3" fill="var(--brand-blue)"/>
    </svg>
    <div class="site-url">www.brindleharbor.com</div>
  </section>

  <section class="card card--back">
    <div class="wordmark">Brindle Harbor</div>
    <div class="contact contact__name">DORIAN VALE</div>
    <div class="contact contact__title">MANAGING DIRECTOR</div>
    <div class="contact contact__address">Brindle Harbor, KLMRUT,456,VO Marlow.</div>
    <div class="contact contact__lines">
      <span><b>P</b> : +000-000-0000</span>
      <span><b>F</b> : +000-000-0000</span>
      <span><b>E</b> : name@email.com</span>
    </div>
    <svg class="footer-band" viewBox="0 0 525 60" aria-hidden="true">
      <rect x="72" y="3" width="380" height="55" fill="var(--brand-red)"/>
      <rect x="0" y="56" width="525" height="3" fill="var(--brand-blue)"/>
    </svg>
    <div class="site-url">www.brindleharbor.com</div>
  </section>

</main>
</body>
</html>
```